Moonlit Cadence - lifestyle coaching for women looking for D/s dynamic

Create website design and logo based on the requirements in the creative brief file.

Executive summary:
Company Info
Moonlit Cadence is a new life and intimacy coaching company founded by a life and fitness coach. The company focuses on integrating power exchange dynamics into intimate relationships, based on the founder’s personal journey.

Product
The company offers subscription-based online coaching programs with online class structure provided through a learning management system.
Customer Profile
• Target Audience: Women aged 45-55
• Customer needs: see appendix 1
• Language: English-speaking
• Economic Status: Middle to upper class
• Device Usage: Predominantly mobile (iOS and Android)

Target Market(s)

• Target Audience: Women aged 45-55 • Customer needs: see appendix 1 • Language: English-speaking • Economic Status: Middle to upper class • Device Usage: Predominantly mobile (iOS and Android)

Industry/Entity Type

Personal Development / Lifestyle Coaching

Coding

Coded - Design and coding required

Number of Pages Required

1 page

Font styles to use
Sans Serif

Requirements
Must have
• Lead capture tools, scheduling of intake calls, payment via Stripe, ready to be maintained by WIX or Wordpress
Nice to have
• Blog page

```html
<!DOCTYPE html>
<html lang="en">
<head>
<meta charset="utf-8">
<title>Moonlit Cadence – Life & Intimacy Coaching</title>
<link href="https://fonts.googleapis.com/css2?family=Poppins:wght@400;500;600;700&display=swap" rel="stylesheet">
<style>
:root{
  --teal:#3d6064;
  --teal-dark:#355457;
  --lavender:#ebe7f2;
  --lavender-deep:#a99bc9;
  --ink:#1c1c1c;
  --muted:#6b6b6b;
  --white:#ffffff;
  --gold:#e6c9a4;
}
*{margin:0;padding:0;box-sizing:border-box}
html,body{width:1200px;height:4433px;overflow:hidden}
body{font-family:"Poppins",sans-serif;color:var(--ink);background:var(--white)}
.page{position:relative;width:1200px;height:4433px;overflow:hidden}
.abs{position:absolute}
.btn{position:absolute;display:flex;align-items:center;justify-content:center;background:var(--teal);color:var(--white);border-radius:30px;font-weight:500;text-transform:uppercase;white-space:nowrap}
.section-title{position:absolute;left:0;width:1200px;text-align:center;font-size:38px;font-weight:700;letter-spacing:.5px}
.section-title span{color:var(--teal)}

/* nav */
.nav a{position:absolute;top:56px;font-size:13px;color:var(--ink);text-decoration:none;font-weight:500}
.brand-mark{position:absolute;left:523px;top:0;width:130px;height:130px;border-radius:50%;background:var(--teal);border:5px solid #2f4a4d;display:flex;align-items:center;justify-content:center;text-align:center;color:var(--white);font-size:14px;font-weight:600;line-height:1.2;z-index:3}

/* hero */
.hero-photo{position:absolute;left:0;top:98px;width:1200px;height:729px;background:linear-gradient(100deg,#a99bc9 0%,#b9aed2 40%,#d8d2e4 65%,#9c8fb8 100%)}
.hero-title{position:absolute;left:57px;top:378px;width:600px;font-size:39px;font-weight:600;color:var(--white);line-height:1.25}

/* about */
.about-title{position:absolute;left:67px;top:1118px;font-size:38px;font-weight:700}
.about-title span{color:var(--teal)}
.about-text{position:absolute;left:67px;top:1183px;width:440px;font-size:15px;line-height:26px;color:var(--muted)}
.about-photo{position:absolute;left:545px;top:1003px;width:427px;height:500px;border-radius:30px 70px 30px 70px;background:linear-gradient(160deg,#f7d9b6 0%,#e9c0b0 45%,#c99ac2 100%);border:1px solid #c9bfb4}
.feature{position:absolute;left:923px;display:flex;align-items:center;gap:16px}
.feature-icon{width:100px;height:100px;border-radius:50%;background:var(--teal);border:6px solid #dfe5e6;display:flex;align-items:center;justify-content:center}
.feature-label{font-size:18px;font-weight:700;line-height:22px;text-transform:uppercase}

/* services */
.lav-shape{position:absolute;left:0;top:1905px;width:1200px;height:988px}
.svc{position:absolute;width:340px;text-align:center}
.svc-photo{width:226px;height:226px;border-radius:50%;margin:0 auto}
.svc-label{margin-top:34px;font-size:18px;font-weight:600;text-transform:uppercase}
.arrow{position:absolute}

/* benefits */
.benefit-card{position:absolute;left:127px;top:2450px;width:923px;height:320px;background:var(--white);border-radius:32px;overflow:hidden}
.benefit-photo{position:absolute;left:0;top:0;width:391px;height:320px;background:linear-gradient(180deg,#b8c6d6 0%,#cfd6dc 55%,#a9ad8a 100%)}
.benefit-list{position:absolute;left:435px;top:38px;list-style:none}
.benefit-list li{display:flex;gap:16px;align-items:flex-start;font-size:18px;line-height:22px;color:#4a4a4a;margin-bottom:20px;width:460px}
.benefit-list svg{flex:none;margin-top:2px}

/* testimonials */
.testimonial{position:absolute;top:3090px;width:430px;height:228px;background:var(--white);box-shadow:0 4px 18px rgba(0,0,0,.06);overflow:hidden}
.testimonial .wedge{position:absolute;left:0;top:0}
.stars{position:absolute;left:28px;top:26px;color:var(--gold);font-size:30px;letter-spacing:4px}
.quote-badge{position:absolute;right:22px;top:24px;width:76px;height:76px;border-radius:50%;background:var(--white);display:flex;align-items:center;justify-content:center}
.t-name{position:absolute;left:28px;top:88px;font-size:12px;font-weight:600}
.t-text{position:absolute;left:18px;top:136px;width:340px;font-size:11px;line-height:22px;color:var(--muted)}

/* posts */
.post{position:absolute;top:3543px;width:285px}
.post-photo{width:285px;height:174px}
.post-title{margin-top:32px;padding-left:14px;font-size:17px;line-height:20px;font-weight:400;color:var(--ink)}
.post .btn{font-size:12px;font-weight:600;width:128px;height:34px}

/* footer */
.footer{position:absolute;left:0;top:4005px;width:1200px;height:428px;background:var(--teal)}
.footer-brand{position:absolute;left:63px;top:43px;width:160px;height:160px;border-radius:50%;background:#f0e4d6;border:6px solid #2f4a4d;display:flex;align-items:center;justify-content:center;text-align:center;color:var(--teal);font-size:18px;font-weight:600;line-height:1.2}
.social{position:absolute;top:259px;width:22px;height:22px;border-radius:50%;background:var(--gold)}
.f-head{position:absolute;font-size:24px;font-weight:600;color:var(--white)}
.f-list{position:absolute;list-style:none;color:var(--white);font-size:17px}
.f-list li{height:37px;display:flex;align-items:center;gap:8px}
.f-list li::before{content:"→";font-size:13px;color:var(--gold)}
.f-contact{position:absolute;left:925px;list-style:none;color:var(--white);font-size:15px}
.f-contact li{height:48px;display:flex;align-items:center;gap:14px}
.copyright{position:absolute;left:0;top:395px;width:1200px;text-align:center;color:#e7ecec;font-size:12px}
</style>
</head>
<body>
<div class="page">

  <!-- navigation -->
  <nav class="nav">
    <a style="left:52px">HOME</a>
    <a style="left:152px">ABOUT</a>
    <a style="left:261px">SERVICES</a>
    <a style="left:387px">TESTIMONIALS</a>
    <a style="left:702px">BLOG</a>
    <a style="left:802px">CONTACT</a>
  </nav>
  <div class="brand-mark">Moonlit<br>Cadence</div>
  <div class="btn" style="left:959px;top:48px;width:170px;height:34px;font-size:12px">Free Consultation</div>

  <!-- hero -->
  <div class="hero-photo" role="img" aria-label="Coach smiling during a consultation with a client, soft lavender tint"></div>
  <h1 class="hero-title">TRANSFORMATIVE NEW LIFE AND INTIMACY COACHING COMPANY</h1>
  <div class="btn" style="left:57px;top:572px;width:224px;height:44px;font-size:15px;text-transform:uppercase">Free Consultation</div>

  <!-- about -->
  <h2 class="about-title">ABOUT <span>US</span></h2>
  <p class="about-text">The sun dipped below the horizon, casting a warm golden glow across the tranquil waters of the lake. Birds chirped softly as a gentle breeze rustled the leaves of the nearby trees. In the distance, a small boat drifted lazily, its oars cutting through the glassy surface with soft ripples.</p>
  <div class="btn" style="left:67px;top:1351px;width:180px;height:50px;font-size:19px;font-weight:400">Read More</div>
  <div class="about-photo" role="img" aria-label="Woman stretching in a lavender field at sunset"></div>

  <div class="feature" style="top:1063px">
    <div class="feature-icon"><svg width="50" height="50" viewBox="0 0 50 50" fill="none" stroke="#fff" stroke-width="2.2"><circle cx="25" cy="20" r="13"/><circle cx="25" cy="20" r="8"/><path d="M16 30l-5 14 7-3 4 5 3-11M34 30l5 14-7-3-4 5-3-11"/></svg></div>
    <div class="feature-label">Expert<br>Guidance</div>
  </div>
  <div class="feature" style="top:1208px">
    <div class="feature-icon"><svg width="50" height="50" viewBox="0 0 50 50" fill="none" stroke="#fff" stroke-width="2.2"><rect x="8" y="22" width="8" height="20" rx="1"/><path d="M16 40h18a4 4 0 0 0 4-4l2-10a4 4 0 0 0-4-4h-9l2-8a3 3 0 0 0-6-1l-7 11"/><path d="M28 6v-3M36 9l2-2M20 9l-2-2"/></svg></div>
    <div class="feature-label">Tailored<br>Programs</div>
  </div>
  <div class="feature" style="top:1363px">
    <div class="feature-icon"><svg width="56" height="50" viewBox="0 0 56 50" fill="none" stroke="#fff" stroke-width="2.4"><path d="M28 44C10 31 4 23 4 15a11 11 0 0 1 24-4 11 11 0 0 1 24 4c0 8-6 16-24 29z"/></svg></div>
    <div class="feature-label">Proven<br>Results</div>
  </div>

  <!-- lavender background curve -->
  <svg class="lav-shape" viewBox="0 0 1200 988" preserveAspectRatio="none" aria-hidden="true">
    <path d="M1200 0C900 0 240 60 0 545V988H1200Z" fill="#ebe7f2"/>
  </svg>

  <!-- services -->
  <h2 class="section-title" style="top:1685px">OUR <span>SERVICES</span></h2>
  <svg class="arrow" style="left:50px;top:1910px" width="24" height="32" viewBox="0 0 24 32"><path d="M19 3L6 16l13 13" fill="none" stroke="#3d6064" stroke-width="3.5"/></svg>
  <svg class="arrow" style="left:1113px;top:1910px" width="24" height="32" viewBox="0 0 24 32"><path d="M5 3l13 13L5 29" fill="none" stroke="#3d6064" stroke-width="3.5"/></svg>

  <div class="svc" style="left:58px;top:1813px">
    <div class="svc-photo" role="img" aria-label="Coach at a table with a client in a bright room" style="background:linear-gradient(135deg,#e8e2dc,#b8a89a)"></div>
    <div class="svc-label">Online Coaching</div>
  </div>
  <div class="svc" style="left:430px;top:1813px">
    <div class="svc-photo" role="img" aria-label="Woman with arms outstretched outdoors" style="background:linear-gradient(180deg,#dfe3e6,#b9c0c7)"></div>
    <div class="svc-label">Nutrition Coaching</div>
  </div>
  <div class="svc" style="left:770px;top:1813px">
    <div class="svc-photo" role="img" aria-label="Woman relaxing in a lavender field" style="background:linear-gradient(160deg,#f5d6b4,#d79fc0)"></div>
    <div class="svc-label">, Lifestyle Coaching</div>
  </div>

  <!-- program benefits -->
  <h2 class="section-title" style="top:2282px;left:20px">PROGRAM <span>BENEFITS</span></h2>
  <div class="btn" style="left:523px;top:2355px;width:180px;height:46px;font-size:19px;font-weight:400">Contact Us</div>

  <div class="benefit-card">
    <div class="benefit-photo" role="img" aria-label="Woman in sportswear stretching her arms in a meadow"></div>
    <ul class="benefit-list">
      <li><svg width="38" height="38" viewBox="0 0 38 38"><circle cx="19" cy="19" r="16.5" fill="none" stroke="#3d6064" stroke-width="2.5"/><path d="M11 19h15M20 13l6 6-6 6" fill="none" stroke="#3d6064" stroke-width="2.5"/></svg><span>helping individuals foster deeper relationships, self-awareness, and life satisfaction.</span></li>
      <li><svg width="38" height="38" viewBox="0 0 38 38"><circle cx="19" cy="19" r="16.5" fill="none" stroke="#3d6064" stroke-width="2.5"/><path d="M11 19h15M20 13l6 6-6 6" fill="none" stroke="#3d6064" stroke-width="2.5"/></svg><span>Our coaching methods are backed by client success stories</span></li>
      <li><svg width="38" height="38" viewBox="0 0 38 38"><circle cx="19" cy="19" r="16.5" fill="none" stroke="#3d6064" stroke-width="2.5"/><path d="M11 19h15M20 13l6 6-6 6" fill="none" stroke="#3d6064" stroke-width="2.5"/></svg><span>Our mission is to empower you to live your best life, improve your relationships</span></li>
      <li><svg width="38" height="38" viewBox="0 0 38 38"><circle cx="19" cy="19" r="16.5" fill="none" stroke="#3d6064" stroke-width="2.5"/><path d="M11 19h15M20 13l6 6-6 6" fill="none" stroke="#3d6064" stroke-width="2.5"/></svg><span>unlock your full potential with confidence and clarity.</span></li>
    </ul>
  </div>

  <!-- success stories -->
  <h2 class="section-title" style="top:2978px;left:-6px">SUCCESS <span>STORIES</span></h2>
  <svg class="arrow" style="left:62px;top:3190px" width="24" height="32" viewBox="0 0 24 32"><path d="M19 3L6 16l13 13" fill="none" stroke="#3d6064" stroke-width="3.5"/></svg>
  <svg class="arrow" style="left:1125px;top:3190px" width="24" height="32" viewBox="0 0 24 32"><path d="M5 3l13 13L5 29" fill="none" stroke="#3d6064" stroke-width="3.5"/></svg>

  <div class="testimonial" style="left:147px">
    <svg class="wedge" width="430" height="140" viewBox="0 0 430 140"><path d="M0 0H430V140Z" fill="#ebe7f2"/></svg>
    <div class="stars">★★★★★</div>
    <div class="quote-badge"><svg width="40" height="30" viewBox="0 0 40 30" fill="#3d6064"><path d="M2 28V16C2 8 6 3 14 1l1 4c-4 2-6 5-6 9h6v14zM22 28V16c0-8 4-13 12-15l1 4c-4 2-6 5-6 9h6v14z"/></svg></div>
    <div class="t-name">DANA WHITLOW</div>
    <p class="t-text">There are many variations of passages of Lorem Ipsum available, but the majority have suffered alteration in some form, by injected humour, randomised words .</p>
  </div>
  <div class="testimonial" style="left:653px">
    <svg class="wedge" width="430" height="140" viewBox="0 0 430 140"><path d="M0 0H430V140Z" fill="#ebe7f2"/></svg>
    <div class="stars">★★★★★</div>
    <div class="quote-badge"><svg width="40" height="30" viewBox="0 0 40 30" fill="#3d6064"><path d="M2 28V16C2 8 6 3 14 1l1 4c-4 2-6 5-6 9h6v14zM22 28V16c0-8 4-13 12-15l1 4c-4 2-6 5-6 9h6v14z"/></svg></div>
    <div class="t-name">DANA WHITLOW</div>
    <p class="t-text">There are many variations of passages of Lorem Ipsum available, but the majority have suffered alteration in some form, by injected humour, randomised words .</p>
  </div>

  <!-- recent posts -->
  <h2 class="section-title" style="top:3433px;left:12px">RECENT <span>POSTS</span></h2>
  <article class="post" style="left:134px">
    <div class="post-photo" role="img" aria-label="Two men looking at a laptop with a search illustration" style="background:linear-gradient(135deg,#9a9a9a,#d8d8d8 60%,#bfe3ee)"></div>
    <h3 class="post-title">How Life Coaching Can Deepen Your Relationships</h3>
    <div class="btn" style="left:11px;top:305px">Learn More</div>
  </article>
  <article class="post" style="left:466px">
    <div class="post-photo" role="img" aria-label="Desk with coffee and a hand-drawn landing page sketch" style="background:linear-gradient(135deg,#3a3028,#d7c8a8 45%,#e9eef6)"></div>
    <h3 class="post-title">The Benefits of a Holistic Approach to Life and Intimacy Coaching</h3>
    <div class="btn" style="left:12px;top:305px">Learn More</div>
  </article>
  <article class="post" style="left:798px">
    <div class="post-photo" role="img" aria-label="Desk calendar beside a keyboard on a wooden table" style="background:linear-gradient(135deg,#e6e6e6,#d6c3a8 55%,#a88d6e)"></div>
    <h3 class="post-title">How Intimacy Coaching Enhances Your Personal and Emotional Well-being</h3>
    <div class="btn" style="left:20px;top:305px">Learn More</div>
  </article>

  <!-- footer -->
  <footer class="footer">
    <div class="footer-brand">Moonlit<br>Cadence</div>
    <span class="social" style="left:76px" aria-label="Social link"></span>
    <span class="social" style="left:132px" aria-label="Social link"></span>
    <span class="social" style="left:190px" aria-label="Social link"></span>

    <div class="f-head" style="left:362px;top:80px">COMPANY</div>
    <ul class="f-list" style="left:372px;top:127px">
      <li>Home</li><li>About</li><li>Services</li><li>Blog</li><li>Contact</li>
    </ul>

    <div class="f-head" style="left:612px;top:80px">QUICK LINKS</div>
    <ul class="f-list" style="left:636px;top:136px">
      <li>Pricing</li><li>Get Started</li><li>Privacy Policy</li><li>Client Login</li><li>Terms &amp; Conditions</li>
    </ul>

    <div class="f-head" style="left:925px;top:84px">CONTACT</div>
    <ul class="f-contact" style="top:143px">
      <li><svg width="20" height="20" viewBox="0 0 20 20" fill="#e6c9a4"><path d="M4 1l4 4-2 3c1 3 3 5 6 6l3-2 4 4-3 3C8 19 1 12 1 4z"/></svg>1-800-555-0142</li>
      <li><svg width="20" height="16" viewBox="0 0 20 16"><rect x="1" y="1" width="18" height="14" rx="1" fill="#e6c9a4"/><path d="M1 2l9 7 9-7" fill="none" stroke="#3d6064" stroke-width="1.6"/></svg>hello@moonlitcadence.com</li>
      <li><svg width="18" height="22" viewBox="0 0 18 22"><path d="M9 1a8 8 0 0 1 8 8c0 6-8 12-8 12S1 15 1 9a8 8 0 0 1 8-8z" fill="#e6c9a4"/><circle cx="9" cy="9" r="3" fill="#3d6064"/></svg>18 Willow Lane, Avondale</li>
    </ul>

    <p class="copyright">Privacy Policy | © Copyright 2024, All Rights Reserved.</p>
  </footer>

</div>
</body>
</html>
```